Create a Brochure Design for Brantley Homecare

Brantley Homecare is a subsidiary of the Brantley Care Group. This brochure is specifically for the Brantley Homecare company and brand. Create a 3 panel, A4, front and back, tri-fold brochure. This brochure will be a way to introduce our Homecare services to the community, prospective clients, and various referral partners. The brochure must be eye catching, unique in its deliverables and demonstrate both attention to detail and comfort. Our organization is sophisticated and built around warmth, care and individualized personal attention. The most important aspect of this design is to focus on creating a nurturing, warm, and inviting feel where you would want to have a Nurse or Nurse’s Aide in your own home or a loved one’s home.

I am open to the creativity of the designer to develop something based on the above criteria; however I would like the design to work well with the existing collateral material. What I mean by that is that while I want everything to have its own personality and stand out as its own brand representative, I still need to be able to tell that the overall design concept stays stylistically inside of the same ‘family’ of existing designed material. Because of this, below I would like for the designer to pull inspiration from the link to our website (Located below) as well as from the attachment of our recently refreshed business cards (Attached). This should allow each design to be unique and creative, while still staying inside of a framework and the feel/style that I am looking for.

Finally, I want all the designers to understand that this brochure design is for a private, in home, healthcare company where we are responsible for providing personalized care for a culturally and ethnically diverse make-up clientele of all ages. The photos that are used must represent an image of warmth, care, and a positive interaction between client and caregiver.

Look under the Brantley Homecare tab at www.brantleycaregroup-example.net

Industry/Entity Type

Healthcare

Requirements
Must have
• • The Brantley Homecare company logo must be included.

```html
<!DOCTYPE html>
<html lang="en">
<head>
<meta charset="utf-8">
<title>Brantley Homecare Tri-fold Brochure</title>
<link href="https://fonts.googleapis.com/css2?family=PT+Sans:ital,wght@0,400;0,700;1,400&display=swap" rel="stylesheet">
<style>
:root{
  --teal:#0f6a66;
  --teal-dark:#0a4f4c;
  --salmon:#f2716a;
  --salmon-soft:#f9cfc9;
  --blush:#fdeeea;
  --mint:#d3ebe4;
  --ink:#2b2b2b;
  --grey:#5d5d5d;
  --bg:#e9e9e9;
  --charcoal:#1e1e1e;
}
*{box-sizing:border-box;margin:0;padding:0}
html,body{width:1200px;height:1084px;overflow:hidden}
body{background:var(--bg);font-family:"PT Sans",Arial,sans-serif;color:var(--ink);position:relative}
.spread{position:absolute;left:40px;width:1120px;height:510px;background:#fff;display:grid;grid-template-columns:repeat(3,1fr);overflow:hidden;box-shadow:0 4px 18px rgba(0,0,0,.25)}
.spread--outside{top:22px}
.spread--inside{top:552px}
.panel{position:relative;padding:14px 16px 0;border-right:1px solid #e3e3e3;overflow:hidden}
.panel:last-child{border-right:none}
.top-band{position:absolute;top:0;left:0;right:0;height:12px;background:var(--mint)}
.logo{display:flex;align-items:center;justify-content:flex-end;gap:5px;margin-top:8px;height:26px}
.logo__mark{width:12px;height:12px;background:var(--salmon)}
.logo__name{font-weight:700;font-size:17px;color:var(--teal)}
.teal-box{background:var(--teal);color:#fff;border-radius:0 14px 0 14px;padding:9px 11px;font-size:9.5px;line-height:1.35;margin-top:10px}
.teal-box p+p{margin-top:6px}
.label{color:var(--salmon);font-weight:700}
.photo{display:block;background:linear-gradient(135deg,#e9d4c4,#b89580 60%,#7c6a63)}
.photo-row{display:flex;gap:4px;margin:10px -16px 0;height:76px}
.photo-row .photo{flex:1}
.schedule{position:absolute;left:0;right:0;top:248px;bottom:0;background:var(--teal);color:#fff;padding:10px 16px;font-size:9.4px;line-height:1.38}
.schedule h2{color:var(--salmon);font-size:17px;margin-bottom:4px}
.qa h3{font-size:10px;font-weight:700;margin-top:14px}
.qa p{font-size:9.2px;line-height:1.38;margin-top:3px}
.contact{position:absolute;left:0;right:0;top:300px;height:112px;background:var(--salmon);color:#fff;text-align:center;padding-top:14px;font-size:8.6px;line-height:1.45}
.contact h2{font-size:14px;letter-spacing:.5px;margin-bottom:6px}
.cover-logo{position:absolute;top:14px;right:16px;background:#fff;padding:4px 10px}
.cover-logo .logo__name{font-size:24px}
.cover-photo{position:absolute;left:0;right:0;top:62px;height:360px;background:linear-gradient(160deg,#f3e6d8,#d7b9a1 45%,#9a7c6a 85%)}
.tagline{position:absolute;right:22px;top:330px;color:#fff;font-style:italic;font-size:17px;line-height:1.3;text-align:right;text-shadow:0 1px 3px rgba(0,0,0,.35)}
.swoosh{position:absolute;left:0;bottom:0;width:1120px;height:110px;pointer-events:none}
.body-text{font-size:9.2px;line-height:1.4;color:var(--grey)}
.body-text+.body-text{margin-top:7px}
.salmon-text{color:var(--salmon);font-size:9.4px;line-height:1.4}
.help-photo{position:relative;margin:12px -16px 10px;height:88px}
.help-photo span{position:absolute;left:120px;top:20px;font-size:13px;color:#222}
.help-photo strong{display:block;font-size:34px;line-height:.9;color:#111}
.heading{color:var(--teal);font-size:19px;font-weight:700;text-align:center;margin:8px 0 8px}
.list-title{font-weight:700;font-size:9.6px;margin-top:10px}
.plain-list{list-style:none;font-size:9.2px;line-height:1.4;color:var(--grey)}
.care-photo{position:absolute;left:16px;right:16px;top:330px;height:86px}
.right-box{background:var(--teal);color:#fff;margin:10px -16px 0;padding:12px 16px;border-radius:0 0 0 28px;font-size:9.4px;line-height:1.4}
.right-box ul{list-style:none;margin-top:3px;padding-left:6px}
.services{margin-top:8px}
.services h2{color:var(--salmon);font-size:18px}
.services p{font-size:9.1px;line-height:1.38;color:var(--grey);margin-top:4px}
.services-photo{position:absolute;left:16px;right:16px;top:362px;height:70px}
</style>
</head>
<body>

<section class="spread spread--outside" aria-label="Brochure outside">
  <div class="top-band"></div>

  <article class="panel">
    <div class="logo"><span class="logo__mark"></span><span class="logo__name">Brantley</span></div>
    <div class="teal-box">
      <p><span class="label">Medication Services</span> – Our licensed nurse will pre-pour your medication in weekly pill containers for a 28-day period.</p>
      <p><span class="label">Transportation Services</span> – Our Care Professionals run errands or escort you to the grocery store, your personal appointments (physician, beautician, therapy), or other outings.</p>
    </div>
    <div class="photo-row">
      <span class="photo" role="img" aria-label="Caregiver smiling with an elderly client"></span>
      <span class="photo" role="img" aria-label="Portrait of a smiling care professional"></span>
    </div>
    <div class="schedule">
      <h2>Your Schedule</h2>
      <p>Brantley Homecare is flexible with your care needs. As you need more or less care, your schedule can be adjusted to accommodate your needs. We have found that a set schedule works best (same days and times each week). This allows you to be able to depend on the same care professional(s) each week. You determine the schedule, from a minimum of four hours per shift to 24 hours of care per day, 7 days per week, 365 days per year. Our Scheduling department is available 24 hours per day.</p>
    </div>
  </article>

  <article class="panel">
    <div class="logo"><span class="logo__mark"></span><span class="logo__name">Brantley</span></div>
    <div class="qa">
      <h3>What makes Brantley Homecare different from other homecare agencies?</h3>
      <p>Answer: Brantley Homecare has earned a reputation in the community for providing compassionate, dependable, high-quality home care services. We employ Care Professionals who embody the Brantley vision of consistent, outstanding service for every client.</p>
    </div>
    <div class="photo-row" style="margin-top:12px">
      <span class="photo" role="img" aria-label="Caregiver sharing a meal with an elderly client"></span>
    </div>
    <div class="qa">
      <h3>Are your employees screened?</h3>
      <p>Answer: All of our Care Professionals are pre-screened and submit to a comprehensive testing and assessment process which includes their criminal and driving abstracts, as well as screenings through Child/Adult Protective Services.</p>
    </div>
    <div class="contact">
      <h2>CONTACT US</h2>
      <p>1450 Harbor View Ave, Suite 210, Lakeside, HI 96700</p>
      <p>Phone (555) 010-4486</p>
      <p>Fax (555) 010-4822</p>
      <p>marian@brantleycare-example.com</p>
    </div>
  </article>

  <article class="panel">
    <div class="cover-logo logo"><span class="logo__mark"></span><span class="logo__name">Brantley</span></div>
    <div class="cover-photo" role="img" aria-label="Caregiver serving breakfast to an elderly woman at home"></div>
    <p class="tagline">Some one you can depend<br>on without question......</p>
  </article>

  <svg class="swoosh" viewBox="0 0 1120 110" preserveAspectRatio="none" aria-hidden="true">
    <path d="M0 70 C250 20 520 40 760 90 L760 110 L0 110Z" fill="#f9cfc9"/>
    <path d="M0 85 C260 40 520 60 760 100 L760 110 L0 110Z" fill="#f2716a"/>
    <path d="M0 96 C260 60 520 78 760 106 L760 110 L0 110Z" fill="#0f6a66"/>
    <path d="M747 110 L747 40 C860 60 980 30 1120 0 L1120 110Z" fill="#1e1e1e"/>
    <path d="M747 60 C860 75 990 45 1120 18" stroke="#f2716a" stroke-width="3" fill="none"/>
  </svg>
</section>

<section class="spread spread--inside" aria-label="Brochure inside">
  <article class="panel">
    <p class="body-text" style="margin-top:10px">Brantley Care Group is a dedicated, locally owned resource for seniors and families. Over the years the Group has grown to include Brantley Homecare, now trusted by thousands of clients. Our focus has stayed on what we do best: take care of those who need us.</p>
    <p class="body-text">Headquartered in Lakeside, the Brantley Care Group's Administrative Offices are located at 1450 Harbor View Ave, Suite 210. The Group serves the island community of Oahu.</p>
    <div class="help-photo photo" role="img" aria-label="Smiling senior man with a caregiver">
      <span>We're here to<strong>help.</strong></span>
    </div>
    <p class="salmon-text">Marian Brantley, founder, president and CEO of Brantley Care Group, discovered the need for dependable, compassionate home care at the side of a loved one. She was seriously injured in an accident. Inspired, in 1996, at the age of 27, she started Brantley Homecare.</p>
  </article>

  <article class="panel">
    <h2 class="heading">Brantley Home Care</h2>
    <p class="body-text">Brantley Homecare is a state-licensed private duty home health care agency serving the island community of Oahu since 1996.</p>
    <p class="body-text">We provide in-home services ranging from light housekeeping to personal care and skilled nursing. We strive to give compassionate, dependable care of the highest quality while maintaining extremely competitive rates. Everything we do is geared toward meeting the individual needs of our clients.</p>
    <p class="body-text">Whether you need a little help or a lot of help, you'll find that Brantley Homecare's services are a cut above the rest. The Brantley Way is special; it is compassionate, professional, dependable, and flexible.</p>
    <p class="list-title">All of our Care Professionals:</p>
    <ul class="plain-list">
      <li>Are bonded, insured and supervised;</li>
      <li>Have passed both criminal and abuse background checks;</li>
      <li>Have been screened for TB;</li>
      <li>Are certified in CPR and First Aid</li>
    </ul>
    <div class="care-photo photo" role="img" aria-label="Nurse caring for a young client"></div>
  </article>

  <article class="panel">
    <div class="logo"><span class="logo__mark"></span><span class="logo__name">Brantley</span></div>
    <div class="right-box">
      <p>All client care is supervised by a licensed Nurse Care Consultant whose duties include:</p>
      <ul>
        <li>Regular home visits</li>
        <li>Client evaluation</li>
        <li>Care Professional supervision</li>
        <li>Revising/updating client care plans</li>
        <li>24/7 phone support</li>
      </ul>
    </div>
    <div class="services">
      <h2>Services</h2>
      <p>Brantley Homecare provides two different levels of care. Our Nurse Care Consultant will assist the client and family in determining the appropriate level of care needed during the complimentary initial consultation.</p>
      <p><span class="label">Nurse Aide Care</span> – Provides personal care needs, companionship, running errands, and light housekeeping, along with assisting you with the activities of daily living.</p>
      <p><span class="label">Skilled Nursing Care</span> – We offer a wide range of skilled nursing services using RN's and LPN's who provide treatment from wound care to life support, in addition to all of the services performed by our Nurse Aides.</p>
    </div>
    <div class="services-photo photo" role="img" aria-label="Caregivers chatting with elderly clients"></div>
  </article>

  <svg class="swoosh" viewBox="0 0 1120 110" preserveAspectRatio="none" aria-hidden="true">
    <path d="M0 60 C200 90 300 40 373 70 L373 110 L0 110Z" fill="#f9cfc9"/>
    <path d="M0 80 C180 100 300 65 373 88 L373 110 L0 110Z" fill="#f2716a"/>
    <path d="M373 95 C520 70 640 100 747 85 L747 110 L373 110Z" fill="#f9cfc9"/>
    <path d="M747 80 C880 100 1000 60 1120 70 L1120 110 L747 110Z" fill="#0f6a66"/>
  </svg>
</section>

</body>
</html>
```